Flyer for cleaning services with special cut and space for general awareness

We need one flyer for cleaning services marketing. Its 2 page flyer preferred to have a special design [attracting people] . Colours should be from our brand guidelines.
We need a space in the flyer to paste one small ' hand wipes' with a general awareness of cleanliness.This flyer can be DL size . But we prefer to have a special design cut which attract people
Our services are
Office /Residential cleaning services
Deep cleaning
Move in /Move out
Carpet shampooing
Villa general cleaning
Apartment general cleaning
Event cleaning

Target Market(s)

Dubai

Industry/Entity Type

Cleaning Service

Font styles to use
Serif
Sans Serif

Requirements
Must have
• Brand guideline colours ,our staff photos
Nice to have
• Special design. cut [for Eg: shape of some cleaning equip]

```html
<!DOCTYPE html>
<html lang="en">
<head>
<meta charset="utf-8">
<title>Crescent Facilities – Cleaning Services Flyer</title>
<link rel="stylesheet" href="https://fonts.googleapis.com/css2?family=Montserrat:wght@600;800;900&family=Open+Sans:wght@400;600&family=Cairo:wght@700&display=swap">
<style>
:root{
  --bg:#8e8e8e;
  --paper:#ffffff;
  --navy:#1f2a6b;
  --purple:#6c3bc4;
  --violet:#7b45d0;
  --blue:#1f8be0;
  --sky:#cfe7fb;
  --red:#ee1c25;
  --ink:#1b1b2e;
  --badge:#c9cdd6;
}
*{box-sizing:border-box;margin:0;padding:0}
html,body{width:1200px;height:1200px;overflow:hidden;background:var(--bg)}
.spread{position:relative;width:1200px;height:1200px;display:flex;gap:40px;justify-content:center;align-items:center}
.flyer{position:relative;width:520px;height:1092px;background:var(--paper);overflow:hidden;box-shadow:0 6px 18px rgba(0,0,0,.25);font-family:"Open Sans",sans-serif}
.hero{position:absolute;left:0;top:0;width:100%;height:480px;background:linear-gradient(180deg,#fff 0%,#eaf4fd 25%,var(--sky) 60%,#5fb0ee 100%)}
.brand{position:absolute;left:40px;top:44px;display:flex;align-items:center;gap:14px}
.brand-mark{width:34px;height:34px;background:var(--purple)}
.brand-text{display:flex;flex-direction:column;color:var(--navy);font-family:"Montserrat",sans-serif;font-weight:800;line-height:1.1}
.brand-ar{font-family:"Cairo",sans-serif;font-size:24px;direction:rtl;text-align:left}
.brand-en{font-size:24px}
.staff-photo{position:absolute;left:40px;top:140px;width:440px;height:340px;border-radius:6px 6px 0 0;background:linear-gradient(180deg,rgba(31,42,107,.15),rgba(31,42,107,.55))}
.price{position:absolute;right:26px;top:380px;width:150px;height:150px;border-radius:50%;background:var(--red);border:5px solid #fff;box-shadow:0 0 0 3px var(--red);color:#fff;text-align:center;font-family:"Montserrat",sans-serif;font-weight:900;display:flex;flex-direction:column;justify-content:center;z-index:3}
.price .cur{font-size:17px}
.price .amt{font-size:46px;line-height:1}
.price .amt small{font-size:15px}
.price .note{font-size:10px;font-weight:600}
.title-band{position:absolute;left:0;top:480px;width:100%;height:100px;background:linear-gradient(90deg,var(--purple),var(--violet) 60%,var(--blue));z-index:2}
.title{position:absolute;left:46px;top:492px;color:#fff;font-family:"Montserrat",sans-serif;font-weight:900;font-size:38px;line-height:1;z-index:3;letter-spacing:.5px}
.services{position:absolute;left:0;top:580px;width:300px;height:320px;padding:26px 20px 0 46px}
.services h2{font-family:"Montserrat",sans-serif;font-weight:900;font-size:19px;color:var(--ink);margin-bottom:10px}
.services ul{list-style:none}
.services li{font-size:15px;color:var(--ink);line-height:29px;padding-left:20px;position:relative}
.services li::before{content:"";position:absolute;left:0;top:11px;width:8px;height:8px;border-radius:50%;background:var(--purple)}
.tiles{position:absolute;right:0;top:580px;width:220px;height:330px;display:flex;flex-direction:column}
.tile{position:relative;flex:1;background:linear-gradient(135deg,#e9eef4,#9fb0c4)}
.tile + .tile{border-top:3px solid #fff}
.tile-label{position:absolute;left:0;bottom:0;width:100%;padding:4px 14px;background:var(--purple);color:#fff;font-family:"Montserrat",sans-serif;font-weight:800;font-size:14px;text-align:right}
.tile:nth-child(2) .tile-label{background:var(--blue)}
.cta{position:absolute;left:0;top:910px;width:360px;height:110px;background:var(--red);color:#fff;padding:14px 0 0 40px;font-family:"Montserrat",sans-serif;font-weight:900}
.cta-head{font-size:44px;line-height:1}
.cta-phone{display:flex;align-items:center;gap:10px;font-size:30px;line-height:1;margin-top:10px}
.cta-side{position:absolute;right:0;top:910px;width:160px;height:110px;background:linear-gradient(135deg,var(--blue),var(--purple))}
.footer{position:absolute;left:0;bottom:0;width:100%;height:72px;background:linear-gradient(90deg,var(--purple),var(--blue));color:#fff;display:flex;align-items:center;justify-content:flex-end;padding-right:34px;font-size:16px;letter-spacing:.5px}

/* back page: shorter call band with a badge strip beneath it */
.flyer--back .tiles{height:320px}
.flyer--back .cta,.flyer--back .cta-side{top:900px;height:100px}
.flyer--back .cta{padding-top:12px}
.badge-strip{position:absolute;left:0;top:1000px;width:100%;height:40px;background:var(--paper);display:flex;align-items:center;gap:10px;padding-left:40px}
.badge{width:26px;height:26px;border-radius:50%;background:var(--badge)}
.badge.sq{border-radius:3px;width:40px}
.flyer--back .footer{height:52px}
</style>
</head>
<body>
<main class="spread">

  <article class="flyer flyer--front">
    <div class="hero"></div>
    <div class="brand">
      <span class="brand-mark"></span>
      <div class="brand-text"><span class="brand-ar">الهلال للمرافق</span><span class="brand-en">Crescent Facilities</span></div>
    </div>
    <div class="staff-photo" role="img" aria-label="Two uniformed cleaning staff holding a caddy of cleaning products and a spray bottle"></div>
    <div class="price"><span class="cur">AED</span><span class="amt">29 / <small>HR</small></span><span class="note">Normal Services</span></div>
    <div class="title-band"></div>
    <h1 class="title">CLEANING<br>SERVICES</h1>
    <section class="services">
      <h2>OUR SERVICES</h2>
      <ul>
        <li>Office cleaning</li><li>Residential cleaning</li><li>Deep cleaning</li><li>Move in /Move out</li>
        <li>Carpet shampooing</li><li>Villa general cleaning</li><li>Apartment general cleaning</li><li>Event cleaning</li>
      </ul>
    </section>
    <div class="tiles">
      <div class="tile" role="img" aria-label="Staff cleaning a kitchen"><span class="tile-label">PROFESSIONAL</span></div>
      <div class="tile" role="img" aria-label="Staff dusting a glass door"><span class="tile-label">AFFORDABLE</span></div>
      <div class="tile" role="img" aria-label="Staff wiping a window"><span class="tile-label">FAST &amp; EFFECTIVE</span></div>
    </div>
    <div class="cta">
      <div class="cta-head">CALL NOW</div>
      <div class="cta-phone">
        <svg width="26" height="26" viewBox="0 0 24 24"><path fill="#fff" d="M6.6 10.8a15 15 0 0 0 6.6 6.6l2.2-2.2c.3-.3.7-.4 1-.2 1.1.4 2.3.6 3.6.6.6 0 1 .4 1 1V20c0 .6-.4 1-1 1A17 17 0 0 1 3 4c0-.6.4-1 1-1h3.5c.6 0 1 .4 1 1 0 1.3.2 2.5.6 3.6.1.3 0 .7-.2 1z"/></svg>
        052 4100726
      </div>
    </div>
    <div class="cta-side"></div>
    <div class="footer">www.crescentfacilities.com</div>
  </article>

  <article class="flyer flyer--back">
    <div class="hero"></div>
    <div class="brand">
      <span class="brand-mark"></span>
      <div class="brand-text"><span class="brand-ar">الهلال للمرافق</span><span class="brand-en">Crescent Facilities</span></div>
    </div>
    <div class="staff-photo" role="img" aria-label="Two uniformed cleaning staff with gloves, a cleaning caddy and a spray bottle"></div>
    <div class="price"><span class="cur">AED</span><span class="amt">29 / <small>HR</small></span><span class="note">Normal Services</span></div>
    <div class="title-band"></div>
    <h1 class="title">CLEANING<br>SERVICES</h1>
    <section class="services">
      <h2>OUR SERVICES</h2>
      <ul>
        <li>Office cleaning</li><li>Residential cleaning</li><li>Deep cleaning</li><li>Move in /Move out</li>
        <li>Carpet shampooing</li><li>Villa general cleaning</li><li>Apartment general cleaning</li><li>Event cleaning</li>
      </ul>
    </section>
    <div class="tiles">
      <div class="tile" role="img" aria-label="Staff cleaning a glass partition"><span class="tile-label">DEEP CLEANINIG</span></div>
      <div class="tile" role="img" aria-label="Staff mopping an office floor"><span class="tile-label">RESPONSIVE</span></div>
      <div class="tile" role="img" aria-label="Staff wiping an office desk"><span class="tile-label">SAFE</span></div>
    </div>
    <div class="cta">
      <div class="cta-head">CALL NOW</div>
      <div class="cta-phone">
        <svg width="26" height="26" viewBox="0 0 24 24"><path fill="#fff" d="M6.6 10.8a15 15 0 0 0 6.6 6.6l2.2-2.2c.3-.3.7-.4 1-.2 1.1.4 2.3.6 3.6.6.6 0 1 .4 1 1V20c0 .6-.4 1-1 1A17 17 0 0 1 3 4c0-.6.4-1 1-1h3.5c.6 0 1 .4 1 1 0 1.3.2 2.5.6 3.6.1.3 0 .7-.2 1z"/></svg>
        052 4100726
      </div>
    </div>
    <div class="cta-side"></div>
    <div class="badge-strip">
      <span class="badge sq"></span><span class="badge sq"></span><span class="badge"></span><span class="badge"></span><span class="badge"></span><span class="badge"></span>
    </div>
    <div class="footer">www.crescentfacilities.com</div>
  </article>

</main>
</body>
</html>
```